Progressive European Honey Business needs minimalistic packaging design

Hello - thank you for your interest in our brief. We are Fizzy Vixens, a London based Honey business, importing only the best honey Europe has to offer. Our values are deeply rooted with in progressive liberal values and we are looking for minimalist packaging, which reflects that.

We are looking for a design, which dimensions fit with our packaging option (Velmor Glass Jar | HEIGHT 90mm | DIAMETER 63mm). We will require a various output files (High Resolution JPEG (CMYK Colors 300 dpi) Source File Ai, PSD, PDF, Printing files (die cut, die folding) and a 3D Mockup of the packaging for use within digital commerce platforms.

We must be able to adjust the free text on the label front and it should include the following:
Brand Name
Honey type
Limited edition No. X / 100 ( X being the number of purchase i.e. 25 / 100)
EU Honey, Single Orgin (Germany)
(c) The net weight (250g)

The back must include room for additional information (again adjustable by us) and the following:
“Unsuitable for children under 12 months”
(b) The appropriate durability declaration

In total, we are looking for
a) A front label
b) A back label
c) A seal (round) including the attached bee and logo included in the Zip file.
Do note that a) & b) can also be combined into one design as long as the symmetry on the jar stays intact.

The final design should communicate modern aesthetics, high quality, that are slightly provocative and pop off the shelves.

Hi folks, sorry for the delay in completing this project, but my business partner had a leak in his house. We planned to finalise our review today, but this will have to wait until it's no longer raining in his livingroom. Our sincere apologies!

• See branding guidelines

• Must follow the branding guideline and fonts provided as attachment

```html
<!DOCTYPE html>
<html lang="en">
<head>
<meta charset="utf-8">
<title>Fizzy Vixens – Front Label</title>
<link rel="stylesheet" href="https://fonts.googleapis.com/css2?family=Barlow+Condensed:wght@600&family=Inter:wght@400&display=swap">
<style>
  :root {
    --page: #ffffff;
    --label-white: #f2eff0;
    --comb-dark: #b07a3e;
    --comb-mid: #d7a868;
    --seal-gold: #e8bd48;
    --seal-stripe: #f1cd4f;
    --seal-white: #f4f1f2;
    --seal-dark: #3b3b3b;
    --ink: #2b2b2b;
    --ink-light: #f1f1f1;
  }
  * { margin: 0; padding: 0; box-sizing: border-box; }
  html, body { width: 1014px; height: 1200px; overflow: hidden; background: var(--page); }
  .canvas { position: relative; width: 1014px; height: 1200px; background: var(--page); }

  .label {
    position: absolute; left: 27px; top: 380px; width: 960px; height: 440px;
    background: var(--label-white); overflow: hidden;
  }
  .label__comb {
    position: absolute; left: 0; top: 0; width: 100%; height: 230px;
    background: linear-gradient(180deg, var(--comb-dark) 0%, var(--comb-mid) 55%, var(--label-white) 100%);
  }
  .label__stripe {
    position: absolute; left: 430px; top: 0; width: 100px; height: 120px;
    background: var(--seal-stripe);
  }

  .label__info { position: absolute; font-family: "Inter", sans-serif; color: var(--ink); font-size: 17px; }
  .label__info--left { left: 40px; top: 268px; }
  .label__info--right { right: 40px; top: 268px; text-align: right; }
  .label__rule { width: 160px; height: 2px; background: var(--ink); margin: 22px 0 16px; }
  .label__info--right .label__rule { margin-left: auto; }
  .label__number { font-size: 20px; }

  .seal { position: absolute; left: 290px; top: 40px; width: 380px; height: 380px; }
  .seal svg { display: block; }
  .seal__name {
    position: absolute; left: 0; width: 100%; top: 82px; text-align: center;
    font-family: "Barlow Condensed", sans-serif; font-weight: 600;
    color: var(--seal-dark); font-size: 64px; line-height: 1; letter-spacing: 1px;
    text-transform: uppercase;
  }
  .seal__origin {
    position: absolute; left: 0; width: 100%; top: 232px; text-align: center;
    font-family: "Barlow Condensed", sans-serif; font-weight: 600;
    color: var(--ink-light); font-size: 33px; line-height: 1.2; letter-spacing: 0.5px;
  }
</style>
</head>
<body>
<div class="canvas">
  <section class="label">
    <div class="label__comb" role="img" aria-label="Honeycomb pattern fading from amber to white"></div>
    <div class="label__stripe"></div>

    <div class="label__info label__info--left">
      <p>Limited Edition</p>
      <div class="label__rule"></div>
      <p class="label__number">No. 25 / 100</p>
    </div>
    <div class="label__info label__info--right">
      <p>Net weight</p>
      <div class="label__rule"></div>
      <p class="label__number">250g</p>
    </div>

    <div class="seal">
      <svg width="380" height="380" viewBox="0 0 380 380">
        <defs>
          <clipPath id="seal-inner"><circle cx="190" cy="190" r="146"/></clipPath>
        </defs>
        <circle cx="190" cy="190" r="188" fill="var(--seal-gold)"/>
        <g clip-path="url(#seal-inner)">
          <rect x="0" y="0" width="380" height="212" fill="var(--seal-white)"/>
          <rect x="0" y="212" width="380" height="168" fill="var(--seal-dark)"/>
        </g>
        <circle cx="190" cy="190" r="146" fill="none" stroke="var(--seal-dark)" stroke-width="5"/>
      </svg>
      <h1 class="seal__name">Fizzy<br>Vixens</h1>
      <p class="seal__origin">EU HONEY<br>SINGLE ORGIN</p>
    </div>
  </section>
</div>
</body>
</html>
```